Bully breed rescue website

I need a website for my bully breed rescue. We rescue bully breeds from up and down the east coast of the United States and train them as service dogs for people with limited mobility disabilities. I don't want a lot of white space. I want it to be modern and slick and colorful and still look professional. I want it to be different and have a lot of wow factor. I linked a copy of my logo.

Number of Pages Required

5+ page

Font styles to use
Sans Serif

Colors

Designer to choose colors to be used in the design.

Requirements
Must have
• Moving aspects. Blog and ecommerce.
• 1.) Home page
• 2.) Services- something modular
• 3.) About US
• 4.) Blog
• 5.) Application page
• 6.) Donation page
• 7.) Contact Us
Nice to have
• Large Slider of photos on home page
• vertical menu bar
Should not have
• Lots of white space. Dont want it to look like a template or any other site

```html
<!DOCTYPE html>
<html lang="en">
<head>
<meta charset="utf-8">
<title>Gentle Giants — Rescuing and Training the Bully</title>
<link rel="stylesheet" href="https://fonts.googleapis.com/css2?family=Germania+One&display=swap">
<style>
  :root {
    --mustard: #f0c44a;
    --ink: #141210;
    --accent-red: #e8283a;
    --panel-olive: rgba(110, 92, 44, 0.9);
    --panel-line: #e9dcc0;
    --panel-text: #fbf6ea;
  }
  * { margin: 0; padding: 0; box-sizing: border-box; }
  html, body {
    width: 1200px;
    height: 675px;
    overflow: hidden;
    background: var(--mustard);
  }
  .hero {
    position: relative;
    width: 1200px;
    height: 675px;
    background: var(--mustard);
    font-family: "Germania One", serif;
    overflow: hidden;
  }
  .hero-photo {
    position: absolute;
    inset: 0;
    width: 1200px;
    height: 675px;
  }
  .brand {
    position: absolute;
    left: 26px;
    top: 104px;
    width: 330px;
    text-align: center;
    font-size: 56px;
    line-height: 64px;
    letter-spacing: 1px;
    color: var(--ink);
    white-space: nowrap;
  }
  .tagline-box {
    position: absolute;
    left: 445px;
    top: 261px;
    width: 311px;
    height: 176px;
    background: var(--panel-olive);
    border: 1px solid var(--panel-line);
    outline: 1px solid var(--panel-line);
    outline-offset: -5px;
    padding: 32px 0 0 62px;
  }
  .tagline {
    font-size: 30px;
    line-height: 38px;
    letter-spacing: 1.5px;
    color: var(--panel-text);
    font-weight: 400;
    text-transform: uppercase;
  }
  .main-nav {
    position: absolute;
    left: 46px;
    top: 443px;
  }
  .main-nav ul { list-style: none; }
  .main-nav a {
    display: block;
    font-size: 24px;
    line-height: 30px;
    letter-spacing: 2px;
    text-transform: uppercase;
    text-decoration: none;
    color: var(--ink);
  }
  .main-nav a.is-highlight { color: var(--accent-red); }
</style>
</head>
<body>
  <main class="hero">
    <svg class="hero-photo" viewBox="0 0 1200 675" role="img" aria-label="Photo of a white and grey bully breed dog lying on green grass chewing a bone">
      <defs>
        <linearGradient id="photoTone" x1="1" y1="0" x2="0.25" y2="1">
          <stop offset="0" stop-color="#9cc86a"/>
          <stop offset="0.18" stop-color="#dfe9cf"/>
          <stop offset="0.4" stop-color="#f4f3f0"/>
          <stop offset="0.6" stop-color="#e2d2d2"/>
          <stop offset="0.78" stop-color="#75767b"/>
          <stop offset="1" stop-color="#3a3b40"/>
        </linearGradient>
      </defs>
      <polygon points="828,0 1200,0 1200,675 560,675" fill="url(#photoTone)"/>
    </svg>

    <div class="brand">Gentle Giants</div>

    <section class="tagline-box">
      <h1 class="tagline">Rescuing and<br>training the<br>bully</h1>
    </section>

    <nav class="main-nav">
      <ul>
        <li><a href="#services">Services</a></li>
        <li><a href="#about">About us</a></li>
        <li><a href="#blog">Blog</a></li>
        <li><a href="#applications">Applications</a></li>
        <li><a href="#donations" class="is-highlight">Donations</a></li>
        <li><a href="#contact">Contact us</a></li>
      </ul>
    </nav>
  </main>
</body>
</html>
```